House-share and Room Rental Website (With Focus on the Bedroom Landing Page)

Looking for website design for our House-share (executive accommodation) and room rental business.

Our company name is: Lodvenra could also be written as LodVenra or lodvenra. Either is fine .. just looking for a nice clean catchy logo to go with the design.

EXAMPLES
These are examples of other websites in this field that are doing well. this is a kind of baseline.
https://kelbrin.com.au/
https://www.tuvaplex.com/
https://www.nestorvi.com/
https://www.quillsa.net/
https://www.pendlebarrow.com.au/

Our business model is to rent rooms to people looking for high-quality accommodation. We fill the gap between those looking to rent rooms and those with rooms to rent. However, our model is slightly different from those already on the market as we looking to fill a massive gap in the market delivering upmarket rooms for rent.(Executive Accommodation) also in the back end will be coupled with a self management process in the back end.

We offer executive style accommodation that stands out above the rest. With special extras like fire safety.. and management processes that create happier homes. We are looking for a web design package that can help us grow and scale our business. We need a design that is captivating

Our MAIN focus is having a room landing page that stands out from the rest... The core of our business will rely on the promotion of the rooms in a share house... so the whole design relies on the BEDROOM landing page to drive results.

Target Market(s)

We have 2 markets we are aiming at ... the first market is people offering rooms to rent who want the highest rental return. The second market is people looking to rent safe, high-quality rooms, in houses that are well managed and looked after.

Industry/Entity Type

Share Economy

Logo Text

LodVenra

Number of Pages Required

5+ page

Font styles to use
Sans Serif

Colors
3276b5

Requirements
Must have
• A messaging system whereby we can create direct communication between those offering rooms and those looking for rooms.
• A call to action that says " Schedule an Inspection"
• Landing page for promoting rooms
• A home page for showing stock.
• Profile page for those selling rooms
• Profile page for those looking for rooms.
• A scheduling calendar for booking inspections
Nice to have
• Pages where new residents can lock in a room.. pay bond and rents.. and sign contracts
• Notifications
• SMS capabilities in the backend.
Should not have
• No script or handwriting fonts.

```html
<!DOCTYPE html>
<html lang="en">
<head>
<meta charset="utf-8">
<title>Lodvenra – Executive Accommodation</title>
<link href="https://fonts.googleapis.com/css2?family=Montserrat:wght@400;500;600;700;800&display=swap" rel="stylesheet">
<style>
:root{
  --ink:#1b1b1b;
  --dark:#161616;
  --blue:#1e8fe8;
  --brand:#3276b5;
  --orange:#e6a523;
  --grey-text:#6a6a6a;
  --field-text:#9a9a9a;
  --line:#b9b9b9;
  --band:#eceef1;
  --white:#ffffff;
}
*{box-sizing:border-box;margin:0;padding:0}
html,body{width:822px;height:1200px;overflow:hidden;background:var(--white);font-family:'Montserrat',sans-serif;color:var(--ink)}
.page{position:relative;width:822px;height:1200px}
.abs{position:absolute}

/* header */
.site-header{left:0;top:0;width:822px;height:37px;background:var(--dark)}
.brand{left:114px;top:4px;display:flex;align-items:center;gap:6px;color:var(--white)}
.brand-dot{width:26px;height:26px;border-radius:50%;background:var(--brand)}
.brand-name{font-size:18px;font-weight:500;line-height:18px}
.brand-tag{font-size:7.5px;font-weight:400;line-height:9px}
.nav{right:130px;top:14px;display:flex;gap:13px;font-size:7px;font-weight:500;color:var(--white);letter-spacing:.1px}
.burger{left:691px;top:13px;width:15px}
.burger span{display:block;height:2.4px;background:var(--white);margin-bottom:2.6px;border-radius:1px}

/* hero */
.hero{left:0;top:37px;width:822px;height:357px;background:linear-gradient(100deg,#3a3a3c 0%,#5c5b5b 40%,#77726d 65%,#4c4a48 100%)}
.hero-title{left:0;top:118px;width:822px;text-align:center;color:var(--white);font-size:19px;font-weight:800;line-height:25px;letter-spacing:.6px}

/* tabs & form */
.tab{top:197px;height:49px;display:flex;align-items:center;justify-content:center;color:var(--white);font-size:13px;font-weight:800;letter-spacing:.3px}
.tab-search{left:126px;width:288px;background:var(--blue);padding-top:6px}
.tab-offer{left:414px;width:282px;background:var(--orange)}
.tab-pointer{left:126px;top:246px}
.panel{left:126px;top:246px;width:570px;height:224px;background:var(--white);box-shadow:0 1px 4px rgba(0,0,0,.22)}
.label{font-size:7.5px;color:#444}
.check{display:flex;align-items:center;gap:6px;font-size:9px;font-weight:700;color:var(--field-text)}
.box{width:11px;height:11px;border:1px solid #999;border-radius:1px;background:var(--white)}
.field{height:28px;border:1px solid var(--line);display:flex;align-items:center;justify-content:space-between;padding:0 7px;font-size:9.5px;font-weight:700;color:var(--field-text);background:var(--white)}
.field svg{width:8px;height:5px}
.submit{left:451px;top:172px;width:101px;height:27px;background:var(--ink);color:var(--white);font-size:9.5px;font-weight:700;display:flex;align-items:center;justify-content:center;border-radius:2px}

/* featured */
.section-title{font-size:15px;font-weight:500}
.city-select{left:610px;top:520px;width:84px;height:18px;border:1px solid #888;font-size:7.5px;color:#555;display:flex;align-items:center;justify-content:space-between;padding:0 6px}
.card{top:562px;width:184px}
.card-photo{width:180px;height:125px}
.card-body{padding:14px 2px 0 2px}
.card-key{font-size:7.5px;font-weight:800;margin-left:2px;line-height:8px}
.card-val{font-size:7.5px;color:var(--grey-text);margin-left:2px;margin-top:4px;margin-bottom:7px}
.card-price{font-size:7.5px;font-weight:800;color:var(--blue);margin-left:2px;margin-top:6px;margin-bottom:8px}
.card-text{font-size:7.8px;line-height:12.5px;color:var(--grey-text);margin-top:6px}
.card-go{width:12px;height:12px;background:var(--orange);display:flex;align-items:center;justify-content:center;margin-left:162px;margin-top:5px}
.slider-arrow{top:676px;width:25px;height:24px;background:#d9d9d9;display:flex;align-items:center;justify-content:center}

/* how it works */
.how{left:0;top:882px;width:822px;height:240px;background:var(--band)}
.step{top:968px;width:180px;text-align:center}
.step-icon{width:60px;height:56px;margin:0 auto;border-radius:8px}
.step-title{font-size:11px;font-weight:500;margin-top:14px}
.step-text{font-size:7.8px;line-height:12.5px;color:var(--grey-text);margin-top:10px;padding:0 4px}

/* footer */
.site-footer{left:0;top:1122px;width:822px;height:38px;background:var(--dark)}
.footer-links{left:118px;top:15px;display:flex;gap:12px;font-size:7px;color:var(--white)}
.social{left:664px;top:14px;display:flex;gap:8px}
.social span{width:10px;height:10px;border-radius:50%;background:var(--blue)}
.copyright{left:0;top:1175px;width:822px;text-align:center;font-size:6.5px;color:#333}
</style>
</head>
<body>
<div class="page">

  <header class="site-header abs">
    <div class="brand abs">
      <span class="brand-dot"></span>
      <div>
        <div class="brand-name">Lodvenra</div>
        <div class="brand-tag">Executive Accommodation</div>
      </div>
    </div>
    <nav class="nav abs"><span>CREATE AN ACCOUNT</span><span>LOGIN</span></nav>
    <div class="burger abs"><span></span><span></span><span></span></div>
  </header>

  <section class="hero abs" role="img" aria-label="Dim modern hotel-style bedroom with a bed, armchair and city view window"></section>
  <h1 class="hero-title abs">WELCOME TO THE EASIEST WAY TO<br>HOUSE-SHARE OR RENT A ROOM</h1>

  <div class="tab tab-search abs">SEARCH FOR A ROOM</div>
  <div class="tab tab-offer abs">OFFER A ROOM</div>

  <form class="panel abs">
    <div class="abs" style="left:16px;top:19px;display:flex;align-items:center;gap:12px">
      <span class="label">I'm a / We are</span>
      <span class="check"><span class="box"></span>Male</span>
      <span class="check"><span class="box"></span>Female</span>
      <span class="check"><span class="box"></span>Couple</span>
    </div>

    <span class="label abs" style="left:18px;top:46px">Looking for Room</span>
    <span class="label abs" style="left:153px;top:46px">City</span>
    <span class="label abs" style="left:287px;top:46px">Size of room</span>
    <span class="label abs" style="left:427px;top:46px">Bathroom</span>
    <div class="field abs" style="left:16px;top:61px;width:129px">Private<svg viewBox="0 0 8 5"><path d="M1 1l3 3 3-3" fill="none" stroke="#333" stroke-width="1.1"/></svg></div>
    <div class="field abs" style="left:152px;top:61px;width:129px">City or postal code</div>
    <div class="field abs" style="left:288px;top:61px;width:129px">Any<svg viewBox="0 0 8 5"><path d="M1 1l3 3 3-3" fill="none" stroke="#333" stroke-width="1.1"/></svg></div>
    <div class="field abs" style="left:424px;top:61px;width:129px">Shared<svg viewBox="0 0 8 5"><path d="M1 1l3 3 3-3" fill="none" stroke="#333" stroke-width="1.1"/></svg></div>

    <span class="label abs" style="left:16px;top:101px">Bed size</span>
    <span class="label abs" style="left:151px;top:101px">Type of housemates</span>
    <span class="label abs" style="left:287px;top:101px">Parking</span>
    <span class="label abs" style="left:425px;top:101px">Minimum contract</span>
    <div class="field abs" style="left:15px;top:116px;width:129px">Any<svg viewBox="0 0 8 5"><path d="M1 1l3 3 3-3" fill="none" stroke="#333" stroke-width="1.1"/></svg></div>
    <div class="field abs" style="left:151px;top:116px;width:129px">Shared<svg viewBox="0 0 8 5"><path d="M1 1l3 3 3-3" fill="none" stroke="#333" stroke-width="1.1"/></svg></div>
    <div class="field abs" style="left:287px;top:116px;width:129px">Street<svg viewBox="0 0 8 5"><path d="M1 1l3 3 3-3" fill="none" stroke="#333" stroke-width="1.1"/></svg></div>
    <div class="field abs" style="left:423px;top:116px;width:129px">3 Months<svg viewBox="0 0 8 5"><path d="M1 1l3 3 3-3" fill="none" stroke="#333" stroke-width="1.1"/></svg></div>

    <span class="label abs" style="left:17px;top:156px">Internet speed</span>
    <div class="field abs" style="left:15px;top:172px;width:129px">50 mbps<svg viewBox="0 0 8 5"><path d="M1 1l3 3 3-3" fill="none" stroke="#333" stroke-width="1.1"/></svg></div>
    <span class="check abs" style="left:151px;top:180px"><span class="box"></span>Smoking</span>
    <span class="check abs" style="left:228px;top:180px"><span class="box"></span>Non-smoking</span>
    <div class="submit abs">Submit</div>
  </form>
  <svg class="tab-pointer abs" width="14" height="10" viewBox="0 0 14 10"><path d="M0 0h14L6 10z" fill="var(--blue)"/></svg>

  <h2 class="section-title abs" style="left:118px;top:518px">Featured Available Rooms</h2>
  <div class="city-select abs">Carverton<svg width="7" height="5" viewBox="0 0 8 5"><path d="M1 1l3 3 3-3" fill="none" stroke="#333" stroke-width="1.1"/></svg></div>

  <div class="slider-arrow abs" style="left:67px"><svg width="10" height="14" viewBox="0 0 10 14"><path d="M8 1L2 7l6 6" fill="none" stroke="#fff" stroke-width="1.4"/></svg></div>
  <div class="slider-arrow abs" style="left:729px"><svg width="10" height="14" viewBox="0 0 10 14"><path d="M2 1l6 6-6 6" fill="none" stroke="#fff" stroke-width="1.4"/></svg></div>

  <article class="card abs" style="left:118px">
    <div class="card-photo" role="img" aria-label="Bright bedroom with a grey upholstered bed and patterned rug" style="background:linear-gradient(160deg,#ddd6cc,#b8a99a 70%,#8c7563)"></div>
    <div class="card-body">
      <div class="card-key">Adress</div>
      <div class="card-val">4096 N Fernwold St,&nbsp; Carverton VA 32101, USA</div>
      <div class="card-key">Rental price</div>
      <div class="card-price">$20.50/Month</div>
      <div class="card-key">Amenities</div>
      <p class="card-text">Lorem ipsum dolor sit amet, consectetur adipiscing elit. Proin rhoncus, erat fringilla viverra egestas, risus massa lacinia felis, eget faucibus est elit id enim.</p>
      <div class="card-go"><svg width="6" height="8" viewBox="0 0 6 8"><path d="M1 1l3 3-3 3" fill="none" stroke="#fff" stroke-width="1.2"/></svg></div>
    </div>
  </article>

  <article class="card abs" style="left:322px">
    <div class="card-photo" role="img" aria-label="Bedroom with a white bed, blue-green quilt and light blue walls" style="background:linear-gradient(160deg,#9fc4cc,#c9d2cc 50%,#8d7c6a)"></div>
    <div class="card-body">
      <div class="card-key">Adress</div>
      <div class="card-val">4096 N Fernwold St,&nbsp; Carverton VA 32101, USA</div>
      <div class="card-key">Rental price</div>
      <div class="card-price">$20.50/Month</div>
      <div class="card-key">Amenities</div>
      <p class="card-text">Lorem ipsum dolor sit amet, consectetur adipiscing elit. Proin rhoncus, erat fringilla viverra egestas, risus massa lacinia felis, eget faucibus est elit id enim.</p>
      <div class="card-go"><svg width="6" height="8" viewBox="0 0 6 8"><path d="M1 1l3 3-3 3" fill="none" stroke="#fff" stroke-width="1.2"/></svg></div>
    </div>
  </article>

  <article class="card abs" style="left:525px">
    <div class="card-photo" role="img" aria-label="Bedroom with a grey headboard and floral white bedding" style="background:linear-gradient(160deg,#e8e8e4,#c9cbc2 55%,#8e8f80)"></div>
    <div class="card-body">
      <div class="card-key">Adress</div>
      <div class="card-val">4096 N Fernwold St,&nbsp; Carverton VA 32101, USA</div>
      <div class="card-key">Rental price</div>
      <div class="card-price">$20.50/Month</div>
      <div class="card-key">Amenities</div>
      <p class="card-text">Lorem ipsum dolor sit amet, consectetur adipiscing elit. Proin rhoncus, erat fringilla viverra egestas, risus massa lacinia felis, eget faucibus est elit id enim.</p>
      <div class="card-go"><svg width="6" height="8" viewBox="0 0 6 8"><path d="M1 1l3 3-3 3" fill="none" stroke="#fff" stroke-width="1.2"/></svg></div>
    </div>
  </article>

  <section class="how abs"></section>
  <h2 class="section-title abs" style="left:0;top:910px;width:822px;text-align:center">How it Works</h2>

  <div class="step abs" style="left:116px">
    <div class="step-icon" role="img" aria-label="Illustration of a house with a magnifying glass" style="background:linear-gradient(135deg,#1e7fd0,#e6a523)"></div>
    <div class="step-title">Start your Serch</div>
    <p class="step-text">Proin rhoncus, erat fringilla viverra egestas, risus massa lacinia felis, eget faucibus est elit id enim.</p>
  </div>
  <div class="step abs" style="left:321px">
    <div class="step-icon" role="img" aria-label="Illustration of an upward arrow, coin and small house" style="background:linear-gradient(135deg,#1e7fd0,#e6a523)"></div>
    <div class="step-title">Upgrade to Premium</div>
    <p class="step-text">Proin rhoncus, erat fringilla viverra egestas, risus massa lacinia felis, eget faucibus est elit id enim.</p>
  </div>
  <div class="step abs" style="left:528px;top:972px">
    <div class="step-icon" role="img" aria-label="Illustration of an open door" style="background:linear-gradient(135deg,#1e7fd0,#e6a523)"></div>
    <div class="step-title">Find a Room</div>
    <p class="step-text">Proin rhoncus, erat fringilla viverra egestas, risus massa lacinia felis, eget faucibus est elit id enim.</p>
  </div>

  <footer class="site-footer abs">
    <div class="footer-links abs"><span>PRIVACY POLICY</span><span>TERMS OF USE</span></div>
    <div class="social abs" aria-label="Social links"><span></span><span></span><span></span></div>
  </footer>
  <p class="copyright abs">copyright 2019 lodvenra.com All Righrs Reserved.</p>

</div>
</body>
</html>
```